Erstellung eines responsiven One-Pagers für mittelständiges Unternehmen im Bauhauptgewerbe
Zielgruppe
Seit fast 30 Jahren sind wir als mittelständiges Unternehmen im Bauhauptgewerbe tätig.
Aufgabenstellung
Die bestehende Webseite soll einen Relaunch bekommen. Dazu entnehmen Sie bitte Bildmaterial und Logo aus der alten Seite. Wir würden gerne daraus einen responsiven One-Pager bauen.
Da die alte Seite jetzt schon 10 Jahre alt ist, würden wir gerne ein neues Design erstellen lassen. Später werden wir es entweder selbst von unserem Programmierer entwickeln lassen oder Sie erstellen uns ein Angebot. Das Design sollte auch so aufgebaut sein, dass es responsive funktionieren würde.

```html
<!DOCTYPE html>
<html lang="de">
<head>
<meta charset="utf-8">
<title>Kernbau Sanierung GmbH</title>
<link href="https://fonts.googleapis.com/css2?family=Raleway:wght@300;400;600;700&family=Roboto+Condensed:wght@400&family=Open+Sans:wght@400&display=swap" rel="stylesheet">
<style>
:root{
  --navy:#17305a;
  --blue:#1f4f9e;
  --mid:#2b5cad;
  --light:#5a8bd0;
  --link:#1f64b4;
  --text:#333;
  --muted:#777;
  --white:#fff;
}
*{box-sizing:border-box;margin:0;padding:0}
html,body{width:1200px;height:2387px;overflow:hidden}
body{font-family:"Raleway",sans-serif;color:var(--text);background:var(--white);position:relative}
.wrap{width:1020px;margin-left:100px;position:relative}

.topbar{height:26px;background:linear-gradient(90deg,#fff,#e6e6e6);font-family:"Open Sans",sans-serif;font-size:11px;color:#333}
.topbar .wrap{display:flex;justify-content:space-between;line-height:26px}

.header{height:85px}
.header .wrap{display:flex;align-items:center;height:85px;justify-content:space-between}
.brand{display:flex;align-items:center;gap:10px;font-weight:700;font-size:20px;color:var(--blue)}
.brand-mark{width:20px;height:20px;background:var(--blue)}
.contacts{display:flex;gap:22px}
.contact-item{display:flex;align-items:center;gap:8px}
.contact-item b{display:block;font-weight:700;font-size:15px;color:var(--link)}
.contact-item span{font-size:13px;color:#888}

.nav{height:44px;background:var(--blue);position:relative}
.nav::after{content:"";position:absolute;right:0;top:0;width:305px;height:44px;background:var(--navy);clip-path:polygon(30px 0,100% 0,100% 100%,0 100%)}
.nav ul{list-style:none;display:flex;height:44px;align-items:center;font-size:13px;color:#fff}
.nav li{padding:0 12px;border-right:1px solid #fff;line-height:12px}
.nav li:last-child{border:0}
.nav li.active{background:var(--navy);font-weight:700;line-height:44px;border:0;padding:0 14px}
.nav .social{position:absolute;right:82px;top:12px;width:20px;height:20px;background:#fff;border-radius:2px;z-index:2}

.hero{height:385px;background:linear-gradient(180deg,#9aa3ad 0%,#c2c8cd 45%,#7f8790 100%);position:relative;text-align:center;color:#fff}
.hero h1{font-weight:300;font-size:50px;padding-top:50px;text-shadow:0 2px 4px rgba(0,0,0,.5)}
.hero h1 strong{display:block;font-weight:700;font-size:56px;margin-top:-6px}
.hero p{font-size:17px;margin-top:4px;text-shadow:0 1px 3px rgba(0,0,0,.8)}
.hero .btns{margin-top:20px;display:flex;justify-content:center;gap:15px}
.btn{display:inline-block;border-radius:22px;color:#fff;font-family:"Roboto Condensed",sans-serif}
.hero .btn{width:168px;height:44px;line-height:44px;font-size:19px}
.btn.dark{background:var(--navy)}
.btn.blue{background:var(--blue)}
.dots{position:absolute;right:88px;top:200px;display:flex;flex-direction:column;gap:5px}
.dots i{width:15px;height:15px;border-radius:50%;background:#fff}

.features{position:absolute;top:484px;left:100px;width:1020px;height:183px;display:flex;color:#fff}
.feature{flex:1;padding:16px 24px}
.feature:nth-child(1){background:var(--navy)}
.feature:nth-child(2){background:var(--blue)}
.feature:nth-child(3){background:var(--mid)}
.feature:nth-child(4){background:var(--light)}
.feature h2{font-weight:300;font-size:30px;margin-bottom:8px}
.feature p,.feature li{font-size:11px;line-height:14px}
.feature ul{list-style:none}
.feature li::before{content:"✔ ";font-size:10px}
.feature h3{font-weight:600;font-size:15px;margin-bottom:8px}
.pill{display:inline-block;margin-top:12px;background:#fff;color:var(--blue);font-family:"Roboto Condensed",sans-serif;font-size:11px;padding:4px 12px;border-radius:12px}

.sec-head{text-align:center}
.sec-head h2{font-weight:400;font-size:31px;color:#222}
.sec-head .sub{font-family:"Roboto Condensed",sans-serif;font-size:15px;color:var(--link);margin-top:6px}
.sec-head .rule{width:58px;height:3px;background:var(--blue);margin:12px auto 0}
.lead{font-style:italic;font-weight:300;font-size:10.5px;color:#888;text-align:center;width:740px;margin:20px auto 0;line-height:14px}

.intro{position:absolute;top:686px;left:0;width:1200px;height:232px}
.intro .sec-head{padding-top:14px}
.signature{width:240px;height:26px;margin:16px auto 0;background:linear-gradient(90deg,#fff,#e8e8e8,#fff)}

.services{position:absolute;top:920px;left:0;width:1200px;height:496px;background:linear-gradient(90deg,#dcdcdc,#f6f6f6 50%,#dcdcdc)}
.services .sec-head{padding-top:34px}
.tabs{position:absolute;top:150px;left:109px;width:1013px;display:flex;gap:9px}
.tab{flex:1;height:32px;line-height:32px;background:var(--blue);color:#fff;text-align:center;font-size:13.5px;font-weight:300}
.tab.active{background:var(--navy);position:relative}
.tab.active::after{content:"";position:absolute;left:14px;bottom:-9px;border:9px solid transparent;border-top-color:var(--navy);border-bottom:0}
.panel{position:absolute;top:182px;left:109px;width:1013px;height:314px;background:#fff}
.panel-text{position:absolute;left:31px;top:24px;width:550px}
.panel-text h3{font-weight:400;font-size:19px;color:#333}
.panel-text h4{font-weight:600;font-size:13px;color:#555;margin-top:14px}
.panel-text p{font-size:10.5px;line-height:13.5px;color:#888;margin-top:6px}
.panel-text .btn{margin-top:20px;background:var(--blue);font-size:14px;padding:0 15px;height:34px;line-height:34px}
.gallery{position:absolute;left:604px;top:0;width:370px}
.gallery .main{height:198px;background:linear-gradient(160deg,#6f8e4a,#a6ab9e 55%,#8f8d85)}
.thumbs{height:48px;background:linear-gradient(90deg,#ddd,#fff);display:flex;gap:4px;padding:7px}
.thumbs i{width:58px;height:34px;background:linear-gradient(#6d7066,#9a9a90)}

.refs{position:absolute;top:1416px;left:0;width:1200px;height:419px}
.refs .sec-head{padding-top:10px}
.ref-row{position:absolute;top:180px;left:131px;display:flex;gap:18px}
.ref-row div{width:224px;height:135px}
.arrow{position:absolute;top:228px}
.ref-btns{position:absolute;top:339px;left:0;width:1200px;display:flex;justify-content:center;gap:10px}
.ref-btns .btn{width:168px;height:36px;line-height:36px;font-size:14px;text-align:center;background:var(--blue)}

.contact{position:absolute;top:1835px;left:0;width:1200px;height:404px;background:linear-gradient(90deg,#e2e2e2,#f7f7f7 50%,#e8e8e8)}
.contact .sec-head{padding-top:18px}
.photo-circle{position:absolute;left:97px;top:110px;width:253px;height:253px;border-radius:50%;background:linear-gradient(150deg,#dfe3e8,#f5f5f5 50%,#4a5a3a)}
.contact-info{position:absolute;left:405px;top:152px}
.contact-info h3{font-weight:400;font-size:18px;color:#555;line-height:20px}
.info-line{display:flex;gap:8px;margin-top:14px;font-size:13px;color:#333;line-height:16px}
.form{position:absolute;left:781px;top:142px;width:339px}
.form label{display:flex;align-items:center;gap:4px;font-family:"Open Sans",sans-serif;font-size:10px;color:#666;margin-bottom:4px}
.form .field{height:30px;background:#fff;margin-bottom:24px}
.form small{display:block;font-family:"Roboto Condensed",sans-serif;font-size:8px;color:#555;line-height:11px}
.form .send{position:absolute;right:-2px;bottom:-4px;width:100px;height:24px;line-height:24px;text-align:center;font-size:15px;background:var(--blue)}

.footer{position:absolute;top:2239px;left:0;width:1200px;height:106px;background:var(--blue);color:#fff}
.foot-brand{position:absolute;left:100px;top:36px;display:flex;align-items:center;gap:10px;font-weight:700;font-size:21px}
.foot-brand i{width:22px;height:22px;background:#fff}
.foot-col{position:absolute;top:15px;font-size:12px;line-height:15px}
.foot-col h4{font-weight:400;font-size:17px;border-bottom:1px solid #fff;padding-bottom:1px;margin-bottom:9px}
.foot-col .cols{display:flex;gap:18px}
.copy{position:absolute;top:2345px;left:0;width:1200px;height:42px;background:var(--navy);color:#fff;text-align:center;font-size:13px;line-height:42px}
</style>
</head>
<body>

<div class="topbar"><div class="wrap"><span>Seit über 20 Jahren: Betoninstandsetzung – Spritzbeton – Brückensanierung – Balkone – Abdichtung</span><span>IMPRESSUM | DATENSCHUTZ</span></div></div>

<header class="header"><div class="wrap">
  <div class="brand"><span class="brand-mark"></span>Kernbau Sanierung GmbH</div>
  <div class="contacts">
    <div class="contact-item"><svg width="20" height="30" viewBox="0 0 20 30"><path d="M10 2a8 8 0 0 0-8 8c0 6 8 17 8 17s8-11 8-17a8 8 0 0 0-8-8z" fill="none" stroke="#1f2f55" stroke-width="3"/><circle cx="10" cy="10" r="3" fill="#1f2f55"/></svg><div><b>Besuchen Sie uns</b><span>Lindenweg 12, 68799 Altbrunn</span></div></div>
    <div class="contact-item"><svg width="36" height="32" viewBox="0 0 36 32"><rect x="12" y="2" width="13" height="28" rx="2" fill="none" stroke="#1f2f55" stroke-width="2.5"/><path d="M7 10q-3 6 0 12M29 10q3 6 0 12" fill="none" stroke="#1f2f55" stroke-width="2"/></svg><div><b>Rufen Sie an</b><span>(0 61 00) 55 18 20</span></div></div>
    <div class="contact-item"><svg width="42" height="32" viewBox="0 0 42 32"><rect x="2" y="4" width="38" height="25" fill="none" stroke="#1f2f55" stroke-width="2.5"/><path d="M2 4l19 15L40 4M2 29l14-13M40 29L26 16" fill="none" stroke="#1f2f55" stroke-width="2"/></svg><div><b>Schreiben Sie uns</b><span>info@kernbau-sanierung.de</span></div></div>
  </div>
</div></header>

<nav class="nav"><div class="wrap"><ul>
  <li class="active">STARTSEITE</li><li>UNTERNEHMEN</li><li>LEISTUNGEN</li><li>REFERENZEN</li><li>KARRIERE</li><li>KONTAKT</li>
</ul></div><span class="social"></span></nav>

<section class="hero" role="img" aria-label="Foto des Firmengebäudes mit Werkstatthalle und Firmenfahrzeugen">
  <h1>Willkommen bei <strong>Kernbau Sanierung</strong></h1>
  <p>Betoninstandsetzung - Spritzbeton - Brückensanierung - Balkone - Abdichtung</p>
  <div class="btns"><span class="btn dark">ÜBER UNS</span><span class="btn blue">KONTAKT</span></div>
  <div class="dots"><i></i><i></i><i></i></div>
</section>

<div class="features">
  <div class="feature"><h2>KONTAKT</h2><p>Lindenweg 12<br>68799 Altbrunn<br><br>Tel. (0 61 00) 55 18 20<br>Fax (0 61 00) 55 18 21<br>Mail: info@kernbau-sanierung.de</p></div>
  <div class="feature"><h2>LEISTUNGEN</h2><ul><li>Brückensanierung &amp; Korrosionsschutz</li><li>Statische Spritzbetonverstärkungen</li><li>Beton- und Balkoninstandsetzung</li><li>Horizontalsperren, Beschichtung</li></ul><span class="pill">ZU DEN LEISTUNGEN</span></div>
  <div class="feature"><h2>ÜBER UNS</h2><p>Als mittelständisches, überregional tätiges Unternehmen dürfen wir uns vorstellen. Wir sind Mitglied der Bau-berufsgenossenschaft in Karlsruhe.</p><span class="pill">ZUM UNTERNEHMEN</span></div>
  <div class="feature"><h2>KARRIERE</h2><h3>Vorarbeiter und Facharbeiter gesucht</h3><p>für die Betonsanierung.<br>Ein Führerschein ist erforderlich.</p><span class="pill">ZU DEN JOBS</span></div>
</div>

<section class="intro">
  <div class="sec-head"><h2>Betonsanierung in Heidelberg, Mannheim &amp; Umgebung</h2><div class="sub">LANGFRISTIGE BETONERHALTUNG DURCH INSTANDSETZUNG UND KORROSIONSSCHUTZ</div><div class="rule"></div></div>
  <p class="lead">Sie sind richtig bei uns wenn wir über folgende Begriffe sprechen. Betonschäden, Balkonschäden, Betonschutz- und Instandsetzung, Betonkosmetik, Betonsanierung, Balkone, Brücken, Brandschäden, SIVV, PCC, SPCC und Spritzbeton. Als Untergrundvorbereitung, bei jeder Instandhaltungs-maßnahme, ist eine Reinigung erforderlich. Hierbei kommt das Sandstrahlen, Druckluftstrahlen, Wasserstrahlen, Fräsen oder Schleifen zum Einsatz.</p>
  <div class="signature" role="img" aria-label="Handschriftlicher Gruß: Wir freuen uns auf Sie"></div>
</section>

<section class="services">
  <div class="sec-head"><h2>Unsere Leistungen</h2><div class="sub">BRÜCKENSANIERUNG - SPRITZBETON - BETONINSTANDSETZUNG - ABDICHTUNG</div><div class="rule"></div></div>
  <div class="tabs"><div class="tab active">Brückensanierung &amp; Korrosionsschutz</div><div class="tab">Statische Spritzbetonverstärkungen</div><div class="tab">Beton- &amp; Balkoninstandsetzung</div><div class="tab">Horizontalsperren, Beschichtung</div></div>
  <div class="panel">
    <div class="panel-text">
      <h3>Brückensanierung und Korrosionsschutz</h3>
      <h4>Brückensanierung</h4>
      <p>Brücken werden durch den zunehmenden Verkehr, besonders durch die Traglast von Lastwagen immer stärker beansprucht. Deshalb ist eine regelmäßige Kontrolle und Ausbesserung der Schäden unverzichtbar. Wir setzen mit unserer langjähriger Erfahrung Brücken kompetent in Stand oder erneuern sie bei Bedarf, um sie für die tägliche Beanspruchung wieder tauglich und sicher zu machen.</p>
      <p style="margin-top:12px">Grundlage für die Instandsetzung von Brückenbauwerken ist die ZTV-ING. Hierbei handelt es sich um zusätzliche technische Vertragsbedingungen und Richtlinien für Ingenieurbauten, Stand: Dezember 2007. Alle verwendeten Produkte für die Ausführung werden geprüft und in der aktuellen BAST-Liste aufgeführt.</p>
      <span class="btn">ERFAHREN SIE MEHR</span>
    </div>
    <div class="gallery">
      <div class="main" role="img" aria-label="Foto einer sanierten Fußgängerbrücke mit Treppe und Geländer"></div>
      <div class="thumbs"><i></i><i></i><i></i></div>
    </div>
  </div>
</section>

<section class="refs">
  <div class="sec-head"><h2>Referenzen</h2><div class="sub">GEHÖREN AUCH SIE DAZU</div><div class="rule"></div></div>
  <p class="lead">Wir führen Objekte in verschiedenen Größenordnung aus. Es werden auch Baustellen als Generalunternehmer ausgeführt. Hierbei arbeiten wir ausschließlich mit langjährigen, zuverlässigen Partnern zusammen (Gerüstbau, Fliesen- Schlosser- Malerarbeiten). Anbei unter anderen folgende Objekte, um sich einen Überblick über unser umfassendes Leistungsspektrum zu verschaffen.</p>
  <svg class="arrow" style="left:97px" width="20" height="32" viewBox="0 0 20 32"><path d="M16 3L4 16l12 13" fill="none" stroke="#1f4f9e" stroke-width="5"/></svg>
  <div class="ref-row">
    <div role="img" aria-label="Foto eines sanierten Hochhauses" style="background:linear-gradient(#bcc3cc,#7d858c)"></div>
    <div role="img" aria-label="Foto einer Tunnelausstellung in einer Halle" style="background:linear-gradient(#b9b3a4,#7e6f58)"></div>
    <div role="img" aria-label="Foto einer Betonbrücke über einem Bach" style="background:linear-gradient(#c8ccd0,#7e8f5e)"></div>
    <div role="img" aria-label="Foto eines Kirchengebäudes mit Kuppel" style="background:linear-gradient(#dde0e4,#9a9a92)"></div>
  </div>
  <svg class="arrow" style="left:1092px" width="20" height="32" viewBox="0 0 20 32"><path d="M4 3l12 13L4 29" fill="none" stroke="#1f4f9e" stroke-width="5"/></svg>
  <div class="ref-btns"><span class="btn">GEWERBLICHE OBJEKTE</span><span class="btn">PRIVATE OBJEKTE</span></div>
</section>

<section class="contact">
  <div class="sec-head"><h2>Kontaktieren Sie uns</h2><div class="sub">MIT UNS HABEN SIE EINEN EXPERTEN GEFUNDEN</div><div class="rule"></div></div>
  <div class="photo-circle" role="img" aria-label="Foto des Firmentransporters"></div>
  <div class="contact-info">
    <h3>Vereinbaren Sie doch gleich mit uns ein<br>kostenloses Erstgespräch.</h3>
    <div class="info-line"><svg width="12" height="18" viewBox="0 0 12 18"><path d="M6 1a5 5 0 0 0-5 5c0 4 5 11 5 11s5-7 5-11a5 5 0 0 0-5-5z" fill="#1f4f9e"/><circle cx="6" cy="6" r="2" fill="#fff"/></svg><span>Kernbau Sanierung GmbH<br>Lindenweg 12, 68799 Altbrunn</span></div>
    <div class="info-line" style="margin-top:18px"><svg width="12" height="18" viewBox="0 0 12 18"><rect x="1" y="1" width="10" height="16" rx="2" fill="none" stroke="#1f4f9e" stroke-width="2"/></svg><span>Tel. (0 61 00) 55 18 20</span></div>
    <div class="info-line"><svg width="14" height="14" viewBox="0 0 14 14"><circle cx="7" cy="7" r="6" fill="none" stroke="#1f4f9e" stroke-width="2"/><path d="M1 7h12M7 1v12" stroke="#1f4f9e" stroke-width="1.5"/></svg><span>kontakt@kernbau-sanierung.de</span></div>
  </div>
  <div class="form">
    <label><svg width="9" height="9" viewBox="0 0 9 9"><circle cx="4.5" cy="2.5" r="2.3" fill="#555"/><path d="M0 9a4.5 4 0 0 1 9 0z" fill="#555"/></svg>Ihr Name*</label><div class="field"></div>
    <label><svg width="10" height="9" viewBox="0 0 10 9"><path d="M1 3q4-3 8 0v1H7V3H3v1H1zM2 5h6l1 4H1z" fill="#555"/></svg>Telefonnummer*</label><div class="field"></div>
    <label><svg width="9" height="9" viewBox="0 0 9 9"><circle cx="4.5" cy="2.5" r="2.3" fill="#555"/><path d="M0 9a4.5 4 0 0 1 9 0z" fill="#555"/></svg>Ihr Anliegen*</label><div class="field"></div>
    <small>Die mit * gekennzeichneten Felder sind Pflichtfelder.<br>Ihre Daten werden vertraulich behandelt.</small>
    <span class="btn send">SENDEN</span>
  </div>
</section>

<footer class="footer">
  <div class="foot-brand"><i></i>Kernbau Sanierung GmbH</div>
  <div class="foot-col" style="left:460px;width:303px"><h4>KONTAKT</h4><div class="cols"><span>Kernbau Sanierung GmbH<br>Lindenweg 12<br>68799 Altbrunn</span><span>Tel (0 61 00) 55 18 20<br>Fax (0 61 00) 55 18 21<br>info@kernbau-sanierung.de</span></div></div>
  <div class="foot-col" style="left:842px;width:277px;font-size:10.5px;line-height:12.5px"><h4>NAVIGATION</h4><div class="cols" style="gap:50px"><span><b>STARTSEITE</b><br>UNTERNEHMEN<br>LEISTUNGEN<br>REFERENZEN</span><span>KARRIERE<br>KONTAKT<br>IMPRESSUM<br>DATENSCHUTZ</span></div></div>
</footer>
<div class="copy">© Kernbau Sanierung GmbH 2019</div>

</body>
</html>
```